Flyer Design Project

I am opening a yoga studio called Harbourlight Yoga .Pilates. Fitness
and require a flyer that will be letterbox dropped. It will two sided - DL size.100mm × 210mm

The studio will offer Vinyasa Flow Yoga and Mat Pilates classes. We aim to enable people to lead healthier, happier lives through improved strength, flexibility and general well being that regular yoga and pilates practice offers.

We offer group classes, private and semi private sessions in yoga and pilates.

it must have the logo on it- I have uploaded the logo in two versions - not sure what will look the best.

pick up one of the colours from the logo as the background colour.

Side one:
Simple and clean with one side showing logo and address details, website and with simple intro about studio (if it fits)

Location: 1st Floor, 17 Wattlegrove Parade, Kelsmoor, 3287
phone: 0412 908316
www.harbourlightkelsmoor.com.au

OPENING OCTOBER

other side - class descriptions and intro offer for new clients
$20 for 7 days of classes
$99 for 1 month unlimited.

Class descriptions:
Vinyasa Flow yoga: A class that flows from pose to pose integrating breath, alignment, strength and power. All levels are catered for in a warm room heated to around 26 degrees. You will leave feeling inspired, empowered and energised.

Mat Pilates: A strong, challenging class integrating the key principles of pilates: concentration, control, centring, precision, flowing movement and breath. Using the core as a focus to develop these principles you will be hooked on the physical freedom you experience post workout:improved strength, flexibility and vitality that pilates offers.

Private and semi Private tuition available.

Target Market(s)

mainly women, athletic, 35-55 age, middle class, well educated

Industry/Entity Type

Fitness

Requirements
Must have
• 2 pages
the logo

Should not have
• no pics

```html
<!DOCTYPE html>
<html lang="en">
<head>
<meta charset="utf-8">
<title>Harbourlight Yoga .Pilates. Fitness – DL Flyer</title>
<link rel="stylesheet" href="https://fonts.googleapis.com/css2?family=Source+Sans+3:ital,wght@0,400;0,600;0,700;1,600;1,700&display=swap">
<style>
  :root {
    --sky: #0bb7e6;
    --ink: #111417;
    --paper: #ffffff;
    --brand-grey: #5b5d60;
    --alert-red: #ee1b24;
    --edge: #2a3a44;
  }
  * { box-sizing: border-box; margin: 0; padding: 0; }
  html, body {
    width: 1200px; height: 848px; overflow: hidden;
    background: var(--paper);
    font-family: "Source Sans 3", Arial, sans-serif;
    color: var(--ink);
  }
  .canvas { position: relative; width: 1200px; height: 848px; }

  .flyer-side {
    position: absolute; top: 88px;
    width: 284px; height: 596px;
    background: var(--sky);
    border: 1px solid var(--edge);
  }
  .flyer-front { left: 207px; }
  .flyer-back { left: 646px; }

  /* Front */
  .brand-box {
    position: absolute; left: 12px; top: 11px;
    width: 258px; height: 172px;
    background: var(--paper);
    display: flex; align-items: center; justify-content: center;
    padding: 0 20px;
  }
  .brand-name {
    color: var(--brand-grey); font-weight: 600;
    font-size: 24px; line-height: 1.2; text-align: center;
  }

  .address {
    position: absolute; left: 0; right: 0; top: 207px;
    text-align: center; font-size: 19.5px; line-height: 24px;
  }
  .phone {
    position: absolute; left: 0; right: 0; top: 263px;
    display: flex; justify-content: center; align-items: center; gap: 6px;
    font-size: 22px; font-weight: 700;
  }
  .phone svg { width: 15px; height: 17px; }
  .website {
    position: absolute; left: 0; right: 0; top: 298px;
    text-align: center; font-size: 15px; font-weight: 700; font-style: italic;
  }
  .studio-intro {
    position: absolute; left: 17px; right: 16px; top: 353px;
    font-size: 13.2px; line-height: 16.8px; text-align: justify;
  }
  .studio-intro p + p { margin-top: 16px; }
  .opening-band {
    position: absolute; left: 0; right: 0; bottom: 0; height: 54px;
    background: var(--paper);
    display: flex; align-items: center; justify-content: center;
    color: var(--alert-red); font-weight: 700; font-style: italic;
    font-size: 30px; letter-spacing: -0.2px;
  }

  /* Back */
  .offer-card {
    position: absolute; left: 16px; top: 18px;
    width: 249px; height: 117px;
    background: var(--paper); border-radius: 12px;
    padding: 15px 0 0 8px;
  }
  .offer-title { font-size: 16px; font-weight: 600; font-style: italic; }
  .offer-list { list-style: none; margin: 7px 0 0 10px; font-size: 19px; font-weight: 700; line-height: 27px; }

  .class-label {
    position: absolute; left: 9px;
    height: 24px; width: 155px;
    background: var(--paper); border-radius: 12px;
    padding-left: 8px;
    font-size: 16px; font-weight: 700; font-style: italic; line-height: 24px;
  }
  .label-vinyasa { top: 167px; }
  .label-pilates { top: 329px; }
  .class-copy {
    position: absolute; left: 16px; right: 17px;
    font-size: 13.2px; line-height: 16.8px; text-align: justify; text-indent: 10px;
  }
  .copy-vinyasa { top: 200px; }
  .copy-pilates { top: 360px; }
  .tuition-note {
    position: absolute; left: 0; right: 0; top: 527px;
    text-align: center; font-size: 13.2px;
  }
</style>
</head>
<body>
<main class="canvas">

  <section class="flyer-side flyer-front" aria-label="Flyer front">
    <div class="brand-box">
      <p class="brand-name">Harbourlight Yoga .Pilates. Fitness</p>
    </div>

    <p class="address">1st Floor, 17 Wattlegrove Parade,<br>Kelsmoor, 3287</p>
    <p class="phone">
      <svg viewBox="0 0 16 18" aria-hidden="true"><path d="M4 1 L6.5 5 L4.8 7 C5.8 9.8 7.5 12 10 13.6 L12 12 L15 15 L13 17.2 C7 16.6 1.2 9.5 1.6 3 Z" fill="var(--ink)"/></svg>
      0412 908316
    </p>
    <p class="website">www.harbourlightkelsmoor.com.au</p>

    <div class="studio-intro">
      <p>The studio will offer Vinyasa Flow Yoga and Mat Pilates classes. We aim to enable people to lead healthier, happier lives through improved strength, flexibility and general well being that regular yoga and pilates practice offers.</p>
      <p>We offer group classes, private and semi private sessions in yoga and pilates.</p>
    </div>

    <div class="opening-band">OPENING OCTOBER</div>
  </section>

  <section class="flyer-side flyer-back" aria-label="Flyer back">
    <div class="offer-card">
      <p class="offer-title">Intro offer for new clients:</p>
      <ul class="offer-list">
        <li>$20 for 7 days of classes</li>
        <li>$99 for 1 month unlimited</li>
      </ul>
    </div>

    <h2 class="class-label label-vinyasa">Vinyasa Flow yoga:</h2>
    <p class="class-copy copy-vinyasa">A class that flows from pose to pose integrating breath, alignment, strength and power. All levels are catered for in a warm room heated to around 26 degrees. You will leave feeling inspired, empowered and energised.</p>

    <h2 class="class-label label-pilates">Mat Pilates:</h2>
    <p class="class-copy copy-pilates">A strong, challenging class integrating the key principles of pilates: concentration, control, centring, precision, flowing movement and breath. Using the core as a focus to develop these principles you will be hooked on the physical freedom you experience post workout:improved strength, flexibility and vitality that pilates offers.</p>

    <p class="tuition-note">Private and semi Private tuition available.</p>
  </section>

</main>
</body>
</html>
```